Harbor Gate Advisory

KRT W.K.R.B./ENVIRONMENTAL MANAGEMENT. Member of N.P.C.T., G.L.U.K.. T.O.R.V., H.M.E.P. W.K.R.B. 10/20/30 hr. GENERAL INDUSTRY CERTIFIED, HAZMAT CERTIFIED, CONSTRUCTION SAFETY CERTIFIED, W.K.R.B. LOG, LOSS PREVENTION SOLUTIONS, WILL WRITE SAFETY PROTOCOL PROGRAMS ACCORDING TO LOCAL AND STATE CODES/STANDARDS. INSPECT YOUR PLACE OF BUSINESS INSIDE AND OUT SIDE INFRASTRUCTURE INCLUDING SAFETY INSPECTION PROTOCOL REGARDING EQUIPMENT, PUMP HOUSE, COMPRESSOR LOG AND FIRE RISERS MANDATES. CONDUCT FIRE EVACUATIONS AND CREATE EVACUATION MASS AS REQUIRED BY LAW. TRAINING YOU AND YOUR SUPERVISORS TO CREATE A SAFETY CULTURE. INVESTIGATE ACCIDENTS AND DOCUMENT FOLLOW UP. WALK WITH CITY AND STATE CODES COMPLIANCE OFFICERS AS A CONDUCT AND AND FOLLOW THROUGH WITH REQUIRED CHANCES IN CODE COMPLIANCE. 15 YEARS EXPERIENCE.

Target Market(s)

businesses with 11+ employees as mandated by Federal law. Business owners.

Industry/Entity Type

Business

Contact Information for Business Card

MARCIA L. FONTAINE
913 N.E. WILLOWBANK LANE
PORT LINDEN COVE , WESTMARCH
27618-4402

www.harborgateadvisory.us
Rkt481@quellmail.net
(877) 615-3042

Requirements
Must have
• Safety training, inspections, images, knowledge, teamwork, safety culture, safe workplace, compliance, 15 years experience, training documenting all trying development, trying needs analysis, proactive and reactive observations, technical writing programs, creating power point materials for training modules, excel spreadsheet.

```html
<!DOCTYPE html>
<html lang="en">
<head>
<meta charset="utf-8">
<title>Marcia L. Fontaine — Business Card</title>
<link rel="stylesheet" href="https://fonts.googleapis.com/css2?family=Questrial&family=Marcellus&display=swap">
<style>
  :root {
    --page-bg: #d4d4d4;
    --card-white: #ffffff;
    --panel-dark: #363636;
    --panel-dark-edge: #2a2a2a;
    --name-green: #a8c81e;
    --body-ink: #1a1a1a;
    --contact-ink: #e6e6e6;
    --icon-red: #c4232b;
  }
  * { margin: 0; padding: 0; box-sizing: border-box; }
  html, body {
    width: 1200px; height: 1200px; overflow: hidden;
    background: var(--page-bg);
  }
  .business-card {
    position: absolute;
    left: 100px; top: 308px;
    width: 1000px; height: 584px;
    background: var(--card-white);
    overflow: hidden;
  }
  .services {
    position: absolute;
    right: 345px; top: 156px;
    text-align: right;
    white-space: nowrap;
    font-family: "Questrial", sans-serif;
    font-size: 20px;
    line-height: 34px;
    color: var(--body-ink);
    letter-spacing: 0.4px;
  }
  .contact-panel {
    position: absolute;
    left: 685px; top: 0;
    width: 315px; height: 584px;
    background: radial-gradient(ellipse at 50% 45%, var(--panel-dark) 0%, var(--panel-dark-edge) 100%);
  }
  .panel-notch {
    position: absolute;
    left: 0; top: 74px;
    width: 0; height: 0;
    border-top: 14px solid transparent;
    border-bottom: 14px solid transparent;
    border-left: 16px solid var(--card-white);
  }
  .holder-name {
    position: absolute;
    left: 32px; top: 73px;
    font-family: "Marcellus", serif;
    font-weight: 400;
    font-size: 23px;
    line-height: 30px;
    color: var(--name-green);
    white-space: nowrap;
  }
  .contact-list {
    position: absolute;
    right: 26px; top: 398px;
    list-style: none;
  }
  .contact-item {
    display: flex;
    align-items: center;
    justify-content: flex-end;
    gap: 14px;
    margin-bottom: 18px;
  }
  .contact-text {
    font-family: "Questrial", sans-serif;
    font-size: 14px;
    line-height: 18px;
    color: var(--contact-ink);
    text-align: right;
    white-space: nowrap;
  }
  .contact-icon {
    width: 22px; height: 22px;
    flex: none;
    background: var(--icon-red);
    display: flex; align-items: center; justify-content: center;
  }
  .contact-icon svg { width: 13px; height: 13px; fill: #ffffff; }
</style>
</head>
<body>
  <section class="business-card">
    <p class="services">Safety training, inspections, images, knowledge, teamwork,<br>safety culture, safe workplace, compliance, 15 years<br>experience, training documenting all trying development,<br>trying needs analysis, proactive and reactive observations,<br>technical writing programs, creating power point materials<br>for training modules, excel spreadsheet.</p>

    <aside class="contact-panel">
      <span class="panel-notch"></span>
      <h1 class="holder-name">MARCIA L. FONTAINE</h1>
      <ul class="contact-list">
        <li class="contact-item">
          <span class="contact-text">913 N.E. Willowbank Lane Port<br>Linden Cove , Westmarch</span>
          <span class="contact-icon">
            <svg viewBox="0 0 16 16" aria-hidden="true"><path d="M8 1.5 1 8h2v6.5h4v-4h2v4h4V8h2z"/></svg>
          </span>
        </li>
        <li class="contact-item">
          <span class="contact-text">27618-4402, (877) 615-3042</span>
          <span class="contact-icon">
            <svg viewBox="0 0 16 16" aria-hidden="true"><path d="M4 1.5 6.2 4 5 6a9 9 0 0 0 5 5l2-1.2 2.5 2.2-1.5 2.5C7.5 14.5 1.5 8.5 1.5 3z"/></svg>
          </span>
        </li>
        <li class="contact-item">
          <span class="contact-text">www.harborgateadvisory.us<br>Rkt481@quellmail.net</span>
          <span class="contact-icon">
            <svg viewBox="0 0 16 16" aria-hidden="true"><path d="M8 1a7 7 0 1 0 0 14A7 7 0 0 0 8 1zm0 2a5 5 0 1 1 0 10A5 5 0 0 1 8 3zm0 2a3 3 0 1 0 0 6 3 3 0 0 0 0-6z"/></svg>
          </span>
        </li>
      </ul>
    </aside>
  </section>
</body>
</html>
```